I need a simple, classy and stylish business card. I would like it to have a black background with white writing. I would like you to use my logo you designed on the front with the word 'Imagery" used underneath it in the same font. On the back I was thinking of the website at the top 'tomvarley.com' Then my social media accounts, Can you use the instagram, Facebook and twitter logo then my handles?
Please let me know what you think.
Regards Tom
Industry/Entity Type
Business
Requirements
Must have
- Website: www.tomvarley.com
- Social media handles..
- Instagram: @Tom_Varley_Imagery
- Facebook: Tom Varley Imagery
- Twitter: @Tom_Varley
- Email: info@tomvarly.com
- Phone: 0437 581 904

```html
<!DOCTYPE html>
<html lang="en">
<head>
<meta charset="utf-8">
<title>Tom Varley Imagery – Business Card</title>
<link rel="stylesheet" href="https://fonts.googleapis.com/css2?family=Reenie+Beanie&family=Montserrat:wght@400&display=swap">
<style>
  :root {
    --backdrop: #8a5a2e;
    --card-white: #ffffff;
    --card-black: #0b0b0b;
    --ink-dark: #1a1a1a;
    --ink-muted: #555555;
    --ink-light: #f2f2f2;
    --ink-soft: #bfc3c7;
    --badge: #4f7fa3;
  }
  * { margin: 0; padding: 0; box-sizing: border-box; }
  html, body { width: 1200px; height: 913px; overflow: hidden; }
  body {
    background: var(--backdrop);
    position: relative;
    font-family: "Montserrat", sans-serif;
  }
  .card {
    position: absolute;
    top: 320px;
    width: 490px;
    height: 280px;
    border-radius: 16px;
    box-shadow: 0 12px 30px rgba(0,0,0,.35);
    overflow: hidden;
  }
  .card--front { left: 60px; background: var(--card-white); color: var(--ink-dark); }
  .card--back { left: 650px; background: var(--card-black); color: var(--ink-light); }

  /* front */
  .front-mark {
    position: absolute; right: 40px; top: 50px;
    display: flex; align-items: center; gap: 10px;
  }
  .front-mark__dot { width: 18px; height: 18px; border-radius: 50%; background: var(--ink-dark); flex: none; }
  .front-mark__name { font-size: 16px; color: var(--ink-dark); white-space: nowrap; }
  .holder-name {
    position: absolute; left: 36px; top: 150px;
    font-family: "Reenie Beanie", cursive; font-size: 44px; font-weight: 400; line-height: 1;
  }
  .contact-list {
    position: absolute; left: 38px; top: 200px;
    list-style: none; font-size: 14px; color: var(--ink-muted);
  }
  .contact-list li { display: flex; align-items: center; gap: 8px; height: 20px; }
  .contact-list svg { width: 11px; height: 11px; fill: var(--ink-dark); flex: none; }

  /* back */
  .brand {
    position: absolute; left: 56px; top: 96px;
    display: flex; align-items: center; gap: 12px;
  }
  .brand__dot { width: 18px; height: 18px; border-radius: 50%; background: var(--ink-light); flex: none; }
  .brand__name { font-size: 20px; line-height: 1; color: var(--ink-light); white-space: nowrap; }
  .social {
    position: absolute; right: 50px; top: 146px; text-align: right;
  }
  .social__badges { display: flex; gap: 6px; justify-content: flex-end; margin-bottom: 10px; }
  .social__badge { width: 20px; height: 20px; border-radius: 4px; background: var(--badge); }
  .social__handles { list-style: none; font-size: 13px; line-height: 1.5; color: var(--ink-soft); }
</style>
</head>
<body>
  <section class="card card--front" aria-label="Card front">
    <div class="front-mark">
      <span class="front-mark__dot"></span>
      <span class="front-mark__name">Tom Varley Imagery</span>
    </div>
    <h1 class="holder-name">Tom Varley</h1>
    <ul class="contact-list">
      <li><svg viewBox="0 0 12 12" aria-hidden="true"><path d="M2 1h2.5l1 2.5-1.4 1a6 6 0 0 0 3.4 3.4l1-1.4L11 7.5V10a1 1 0 0 1-1 1A9 9 0 0 1 1 2a1 1 0 0 1 1-1z"/></svg>+330 5817-904</li>
      <li><svg viewBox="0 0 12 12" aria-hidden="true"><path d="M1 2.5h10v7H1zM2 3.5v.3l4 2.7 4-2.7v-.3zm0 1.5v3.5h8V5L6 7.7z"/></svg>info@tomvarley.com</li>
      <li><svg viewBox="0 0 12 12" aria-hidden="true"><circle cx="6" cy="6" r="5"/></svg>www.tomvarley.com</li>
    </ul>
  </section>

  <section class="card card--back" aria-label="Card back">
    <div class="brand">
      <span class="brand__dot"></span>
      <p class="brand__name">Tom Varley Imagery</p>
    </div>
    <div class="social">
      <div class="social__badges">
        <span class="social__badge"></span>
        <span class="social__badge"></span>
        <span class="social__badge"></span>
      </div>
      <ul class="social__handles">
        <li>@Tom_Varley_Imagery</li>
        <li>@TomVarleyImagery</li>
        <li>@Tom_Varley</li>
      </ul>
    </div>
  </section>
</body>
</html>
```